Venture Wreckers Book Needs a Cover Design

We need a cover design for Venture Wreckers, Practical Guidance for Faltering Ventures and Doubting Company Founders. We will publish and ebook first (first priority), followed by a hard cover printed book, and then a soft cover book after a few months. The book includes 40 Venture Wreckers and actions owners can implement to counter them and grow. Some examples of killers: self-sabotage, wild optimism, scamming, addictions, burnout, no plan, procrastination, recklessness, haemorrhaging money, etc. We plan to publish the ebook to Pagelume / Tarvelo standards. We want to see designs that convey professionalism, simplicity and creativity.

Target Market(s)

Small and microbusinesses, including start-ups, proprietorships, cottage industries, home-based, single operator, and businesses with or without employees, including corporations and partnerships with fewer than five employees

Industry/Entity Type

Business

Font styles to use
Sans Serif

Colors

Designer to choose colors to be used in the design.

Requirements
Must have
• Uncluttered, professional
• Title: Venture Wreckers
• Subtitle: Practical Guidance for Faltering Ventures and Doubting Company Founders
• Author: Mel Hartigan
Nice to have
• n/a

```html
<!DOCTYPE html>
<html lang="en">
<head>
<meta charset="utf-8">
<title>Venture Wreckers — Mel Hartigan</title>
<link rel="stylesheet" href="https://fonts.googleapis.com/css2?family=Open+Sans:wght@400;600;700;800&display=swap">
<style>
  :root {
    --photo-top: #17130d;
    --photo-mid: #5a5236;
    --photo-warm: #b08a3e;
    --photo-bottom: #3a2814;
    --gold-light: #ffd66a;
    --gold-mid: #f2a21c;
    --gold-deep: #c86f08;
    --title-white: #ffffff;
    --author-ink: #0d0a06;
    --edge-gold: #d9a441;
  }
  html, body {
    margin: 0;
    padding: 0;
    width: 750px;
    height: 1200px;
    overflow: hidden;
    background: #000;
  }
  .cover {
    position: relative;
    width: 750px;
    height: 1200px;
    overflow: hidden;
    font-family: "Open Sans", Arial, sans-serif;
    border-left: 5px solid var(--edge-gold);
    box-sizing: border-box;
  }
  .cover-photo {
    position: absolute;
    inset: 0;
    background: linear-gradient(180deg, var(--photo-top) 0%, var(--photo-mid) 45%, var(--photo-warm) 78%, var(--photo-bottom) 100%);
  }
  .cover-type {
    position: absolute;
    left: -5px;
    top: 0;
    width: 750px;
    height: 1200px;
  }
  .title-top {
    font-weight: 800;
    font-size: 145px;
  }
  .title-bottom {
    font-weight: 400;
    font-size: 186px;
    fill: var(--title-white);
  }
  .subtitle {
    font-weight: 400;
    font-size: 32px;
    fill: var(--title-white);
  }
  .author {
    font-weight: 600;
    font-size: 84px;
    fill: var(--author-ink);
  }
</style>
</head>
<body>
<main class="cover">
  <div class="cover-photo" role="img" aria-label="Photograph area: two rock climbers on a cliff against a sunset sky"></div>

  <svg class="cover-type" viewBox="0 0 750 1200">
    <defs>
      <linearGradient id="gold-fill" x1="0" y1="0" x2="0" y2="1">
        <stop offset="0" stop-color="var(--gold-light)"/>
        <stop offset="0.5" stop-color="var(--gold-mid)"/>
        <stop offset="1" stop-color="var(--gold-deep)"/>
      </linearGradient>
    </defs>
    <text class="title-top" x="377" y="160" text-anchor="middle" fill="url(#gold-fill)" textLength="645" lengthAdjust="spacingAndGlyphs">VENTURE</text>
    <text class="title-bottom" x="377" y="310" text-anchor="middle" textLength="645" lengthAdjust="spacingAndGlyphs">WRECKERS</text>
    <text class="subtitle" x="377" y="386" text-anchor="middle">Practical Guidance for Faltering Ventures</text>
    <text class="subtitle" x="377" y="433" text-anchor="middle">and Doubting Company Founders</text>
    <text class="author" x="378" y="1125" text-anchor="middle" textLength="632" lengthAdjust="spacingAndGlyphs">MEL HARTIGAN</text>
  </svg>
</main>
</body>
</html>
```